依頼詳細
アルコール除菌ジェルのラベルのデザインをお願い致します
サイズはW110mm×H154mm
ラミネート貼り
希望イメージ
シンプル 複雑
単色 カラフル
暗い 明るい
日常 高級
遊び心 厳粛
未来的 伝統的
女性的 男性的
希望する色
緑系
納品ファイル
• イラストレーター形式 (.ai)
補足説明
実際の現在のデザイン(他社)を添付致します。
添付のデザインのOEM製品になり弊社自社品となります
雰囲気を全然違うようにしてください
業務用です
添付の画像にありますKAVELは必要ございません
また発売元は弊社で製造元は別な会社で記載頂くと思います
宜しくお願い致します
容器の画像を添付致しました。
円形のPETボトルになります
販売先は自動車ディーラー様中心となります
■ 選んだ理由

ディーラー様及び通常の販売先において頂けるデザインでした
関係者で3点選びましたが、全員がこの方のデザインが上がりましたので
決定しました

■ 提案者全員のお礼・コメント

沢山の方からデザインをあげて頂き非常に迷いました。
今後もこのサイトを使って新商品のデザインや
容器のデザインをお願いしたいと思いますのでその際は
宜しいお願い致します。今回はありがとうございました

```html
<!DOCTYPE html>
<html lang="ja">
<head>
<meta charset="utf-8">
<title>アルコール除菌ジェル ラベル</title>
<link rel="stylesheet" href="https://fonts.googleapis.com/css2?family=Noto+Sans+JP:wght@400;700;900&display=swap">
<style>
  :root {
    --forest: #14502f;
    --green: #2e8b57;
    --mint-top: #ffffff;
    --mint-mid: #dcefe2;
    --mint-deep: #a8d5b6;
    --band: #2f9a5f;
    --red: #d8232a;
    --paper: #ffffff;
    --ink: #2f4a3a;
    --rule: #9cc2aa;
    --cell: #edf6f0;
  }
  * { margin: 0; padding: 0; box-sizing: border-box; }
  html, body { width: 900px; height: 1200px; overflow: hidden; background: var(--paper); }
  body { font-family: "Noto Sans JP", sans-serif; }
  .label {
    position: relative;
    width: 900px; height: 1200px;
    background: linear-gradient(180deg, var(--mint-top) 0%, var(--mint-mid) 22%, var(--mint-deep) 52%, var(--mint-mid) 66%, var(--paper) 72%);
    overflow: hidden;
  }
  .hands-art {
    position: absolute; left: 300px; top: 90px; width: 300px; height: 230px;
    border-radius: 40px;
    background: radial-gradient(circle at 50% 45%, #ffffff 0%, #e6f4ea 55%, #b3dcc0 100%);
  }
  .volume-badge {
    position: absolute; left: 690px; top: 80px; width: 120px; height: 120px;
    border-radius: 50%; background: var(--green);
    color: #fff; font-weight: 700; font-size: 60px;
    display: flex; align-items: center; justify-content: center;
  }
  .fire-warning {
    position: absolute; left: 670px; top: 218px; width: 160px;
    text-align: center; color: var(--red);
    font-weight: 900; font-size: 28px; line-height: 1.2;
  }
  .fire-warning small { display: block; font-size: 13px; font-weight: 700; }
  .product-kind {
    position: absolute; top: 330px; width: 100%; text-align: center;
    color: var(--forest); font-weight: 900; font-size: 112px; letter-spacing: 2px;
  }
  .product-main {
    position: absolute; top: 465px; width: 100%; text-align: center;
    color: var(--forest); font-weight: 900; font-size: 230px; line-height: 1; letter-spacing: 20px;
  }
  .product-form {
    position: absolute; top: 720px; left: 180px; width: 540px; height: 78px;
    background: var(--band); color: #fff;
    font-weight: 700; font-size: 50px; text-align: center; line-height: 78px; letter-spacing: 6px;
  }
  .spec-table {
    position: absolute; left: 90px; top: 850px; width: 720px;
    border-collapse: collapse; color: var(--ink); font-size: 19px;
  }
  .spec-table th, .spec-table td {
    border: 1.5px solid var(--rule); padding: 8px 12px; text-align: left; font-weight: 400;
  }
  .spec-table th { width: 140px; font-weight: 700; background: var(--cell); }
  .maker {
    position: absolute; left: 90px; top: 1120px; width: 720px;
    display: flex; justify-content: space-between; color: var(--ink); font-size: 18px;
  }
  .maker .company { font-weight: 700; color: var(--forest); }
</style>
</head>
<body>
  <main class="label">
    <div class="hands-art" role="img" aria-label="白い両手を洗うイラスト"></div>
    <div class="volume-badge">1ℓ</div>
    <div class="fire-warning">火気厳禁<small>第四類アルコール類</small></div>
    <h1 class="product-kind">アルコール</h1>
    <div class="product-main">除菌</div>
    <div class="product-form">ジェル</div>
    <table class="spec-table">
      <tr><th>品名</th><td>アルコール除菌ジェル</td></tr>
      <tr><th>成分</th><td>エタノール、水、カルボマー、グリセリン</td></tr>
      <tr><th>使用方法</th><td>適量を手に取り、乾くまでよくすり込んでください。</td></tr>
      <tr><th>内容量</th><td>1000mL</td></tr>
    </table>
    <div class="maker">
      <span>発売元：<span class="company">株式会社ミドリテック</span></span>
      <span>製造元：株式会社ミナセ化成</span>
    </div>
  </main>
</body>
</html>
```